Corvane Electrical Solutions

On one side. LOGO (underneath:) Commercial Industrial Residential

- NAME & CONTACT DETAILS

Marcus T. Hollings
Project Manager

(Cell icon) (441) 582-6197
(Email icon) cvnelectricalsoultions@mailventra.com
(Facebook & Instagram icons )@cvnelectricalsolutions

Other side: LOGO - underneath ELECTRICAL CONSTRUCTION & MAINTENANCE . LED LIGHTING & AUTOMATION . LIFE SAFETY SYSTEMS (FIRE ALARM / SECURITY) . DATA & COMMUNICATION

```html
<!DOCTYPE html>
<html lang="en">
<head>
<meta charset="UTF-8">
<title>Corvane Electrical Solutions – Business Card</title>
<link href="https://fonts.googleapis.com/css2?family=Open+Sans:wght@400;600;700&display=swap" rel="stylesheet">
<style>
  :root {
    --teal: #1d5f74;
    --grey: #5a5a5a;
    --rule: #6b6b6b;
    --card: #ffffff;
    --bg: #e9e9e7;
  }
  * { box-sizing: border-box; margin: 0; padding: 0; }
  html, body { width: 1200px; height: 1200px; overflow: hidden; }
  body {
    background: var(--bg);
    font-family: "Open Sans", sans-serif;
    display: flex; flex-direction: column; align-items: center; justify-content: center;
    gap: 56px;
  }
  .card {
    position: relative;
    width: 900px; height: 514px;
    background: var(--card);
    box-shadow: 0 4px 14px rgba(0,0,0,.12);
  }
  .wordmark {
    position: absolute; left: 0; right: 0;
    display: flex; align-items: center; justify-content: center; gap: 14px;
  }
  .wordmark__mark {
    width: 22px; height: 22px; background: var(--teal);
  }
  .wordmark__name {
    color: var(--teal); font-weight: 600; font-size: 32px; line-height: 1.2;
    white-space: nowrap;
  }

  /* back side */
  .card--back .wordmark { top: 190px; }
  .services {
    position: absolute; left: 40px; right: 40px; top: 270px;
    color: var(--teal); font-size: 14px; text-transform: uppercase;
    letter-spacing: .03em; line-height: 1.9; text-align: center;
    white-space: nowrap;
  }

  /* front side */
  .card--front .wordmark { top: 70px; }
  .sectors {
    position: absolute; left: 0; right: 0; top: 140px; text-align: center;
    color: var(--grey); font-weight: 600; font-size: 21px; letter-spacing: .03em;
  }
  .person {
    position: absolute; right: 540px; top: 262px; text-align: right;
  }
  .person__name { color: var(--teal); font-weight: 700; font-size: 30px; line-height: 1.3; }
  .person__role { color: var(--grey); font-size: 16px; margin-top: 2px; }
  .divider {
    position: absolute; left: 392px; top: 255px; width: 2px; height: 100px; background: var(--rule);
  }
  .contacts {
    position: absolute; left: 420px; top: 272px;
    list-style: none; color: var(--grey); font-size: 21px; line-height: 1.65;
  }
  .contacts li { display: flex; align-items: center; gap: 12px; }
  .contacts svg { flex: none; }
  .social {
    position: absolute; left: 40px; right: 40px; top: 420px;
    display: flex; align-items: center; justify-content: center; gap: 14px;
    color: var(--teal); font-weight: 600; font-size: 21px;
  }
  .social__icon { width: 38px; height: 38px; border-radius: 50%; background: var(--teal); flex: none; }
</style>
</head>
<body>

  <section class="card card--back">
    <div class="wordmark">
      <span class="wordmark__mark"></span>
      <span class="wordmark__name">Corvane Electrical Solutions</span>
    </div>
    <p class="services">
      Electrical Construction &amp; Maintenance / LED Lighting &amp; Automation<br>
      Life Safety Systems (Fire Alarm / Security) / Data &amp; Communication
    </p>
  </section>

  <section class="card card--front">
    <div class="wordmark">
      <span class="wordmark__mark"></span>
      <span class="wordmark__name">Corvane Electrical Solutions</span>
    </div>
    <p class="sectors">Commercial Industrial Residential</p>

    <div class="person">
      <p class="person__name">Marcus T. Hollings</p>
      <p class="person__role">Project Manager</p>
    </div>
    <span class="divider"></span>

    <ul class="contacts">
      <li>
        <svg width="18" height="24" viewBox="0 0 18 24" aria-hidden="true"><rect x="2" y="1" width="14" height="22" rx="2" fill="none" stroke="#1d5f74" stroke-width="2"/><line x1="7" y1="19" x2="11" y2="19" stroke="#1d5f74" stroke-width="2"/></svg>
        (441) 582-6197
      </li>
      <li>
        <svg width="24" height="18" viewBox="0 0 24 18" aria-hidden="true"><rect x="1" y="1" width="22" height="16" fill="none" stroke="#1d5f74" stroke-width="2"/><polyline points="1,1 12,10 23,1" fill="none" stroke="#1d5f74" stroke-width="2"/></svg>
        cvnelectricalsoultions@mailventra.com
      </li>
    </ul>

    <div class="social">
      <span>@cvnelectricalsolutions</span>
      <span class="social__icon" role="img" aria-label="Social network icon"></span>
      <span class="social__icon" role="img" aria-label="Social network icon"></span>
      <span>@cvnelectricalsolutions</span>
    </div>
  </section>

</body>
</html>
```